Miriams Professional Resume

Pls upgrade to make look more effective and perhaps add α photo on it, both options with photo and without would be great. Thanks very much. I would also like the resume so I can edit as well if I need to down the track.

Target Market(s)

This is my professional resume to make it more effective to potential senior hiring managers,

Colors
f04a50

Requirements
Must have
• Professional look.

```html
<!DOCTYPE html>
<html lang="en">
<head>
<meta charset="utf-8">
<title>Miriam Calder – Resume</title>
<link href="https://fonts.googleapis.com/css2?family=Montserrat:wght@500;600;700&family=Lato:wght@400;700&family=Roboto:wght@500;700&display=swap" rel="stylesheet">
<style>
:root{
  --accent:#f04a50;
  --ink:#1d1d1d;
  --paper:#ffffff;
  --rule:#222;
  --bg-mid:#7a7a7a;
  --bg-edge:#5a5a5a;
}
*{box-sizing:border-box;margin:0;padding:0}
html,body{width:1200px;height:3000px;overflow:hidden}
body{
  background:radial-gradient(ellipse at center,var(--bg-mid) 0%,var(--bg-edge) 100%);
  font-family:"Lato",sans-serif;color:var(--ink);position:relative;
}
.page{
  position:absolute;left:238px;width:724px;height:932px;background:var(--paper);
  box-shadow:0 4px 18px rgba(0,0,0,.45);overflow:hidden;
}
.page--one{top:64px}
.page--two{top:1037px}
.page--three{top:2010px}
.page__strip{height:17px;background:var(--accent)}
.page__footer{
  position:absolute;left:0;right:0;bottom:0;height:76px;background:var(--accent);
  color:#fff;display:flex;align-items:center;justify-content:center;
  font-family:"Lato",sans-serif;font-weight:700;font-size:15px;letter-spacing:2.6px;
}
.page--two .page__footer,.page--three .page__footer{height:57px}

/* header */
.profile{position:absolute;left:54px;top:27px;width:617px;height:203px;border:1.5px solid var(--rule)}
.profile__photo{position:absolute;left:31px;top:15px;width:170px;height:170px;border-radius:50%;
  border:2px solid var(--rule);padding:5px;background:#fff}
.profile__photo span{display:block;width:100%;height:100%;border-radius:50%;
  background:linear-gradient(160deg,#d9d6d6 0%,#7a4a48 45%,#c8343a 100%)}
.profile__name{position:absolute;left:243px;top:32px;font-family:"Montserrat",sans-serif;font-weight:600;
  font-size:35px;letter-spacing:1px;color:var(--accent)}
.profile__role{position:absolute;left:244px;top:87px;font-size:15px;line-height:18px}
.profile__contact{position:absolute;left:258px;top:137px;font-size:15px;line-height:20px;list-style:none}
.profile__contact li{display:flex;align-items:center;gap:7px}
.profile__contact svg{width:13px;height:13px;fill:var(--accent)}

.focus-band{position:absolute;left:21px;top:259px;width:683px;height:30px;background:var(--accent);
  color:#fff;font-family:"Montserrat",sans-serif;font-weight:700;font-size:12.2px;
  display:flex;align-items:center;justify-content:center;letter-spacing:.2px}
.summary{position:absolute;left:33px;top:309px;width:656px;font-size:14.1px;line-height:17.4px;text-align:justify}
.summary p{margin-bottom:10px}

.section-title{font-family:"Montserrat",sans-serif;font-weight:600;font-size:21px;color:var(--accent);
  display:flex;align-items:center;gap:14px;letter-spacing:.3px}
.section-title::after{content:"";width:137px;height:4px;background:var(--accent)}
.skills-title{position:absolute;left:32px;top:540px}
.skills{position:absolute;left:33px;top:586px;width:656px;border-collapse:collapse;font-size:13.6px;line-height:14px}
.skills td{border:1.5px solid var(--rule);width:50%;height:45px;padding:8px 28px;vertical-align:top}

/* page two */
.education{position:absolute;left:20px;top:30px;width:680px}
.entry-list{margin:6px 0 0 22px;font-family:"Roboto",sans-serif;font-weight:500;font-size:16px;line-height:19.3px}
.entry-list li{list-style:none;margin-bottom:9px}
.entry-list strong{font-weight:700}
.experience{position:absolute;left:20px;top:267px;width:680px}
.role-head{margin:10px 0 0 14px;padding-left:7px;border-left:4px solid var(--accent);
  font-family:"Roboto",sans-serif;font-weight:500;font-size:16px;line-height:19.5px}
.duties{list-style:none;margin:16px 0 0 12px;font-size:13.6px;line-height:16px}
.duties li{position:relative;padding-left:10px;margin-bottom:11.6px}
.duties li::before{content:"";position:absolute;left:0;top:6px;width:5px;height:5px;border-radius:50%;background:var(--ink)}

/* page three */
.continued{position:absolute;left:20px;top:30px;width:690px}
.continued .role-head{margin:0 0 4px 14px}
.continued .duties{margin:2px 0 8px 12px;font-size:13.4px;line-height:15.8px}
.continued .duties li{margin-bottom:4.6px}
.continued .duties--spaced li{margin-bottom:7px}
.past-roles{list-style:none;margin:2px 0 0 12px;font-family:"Lato",sans-serif;font-weight:700;font-size:15px;line-height:20px}
.past-roles li{position:relative;padding-left:10px;margin-bottom:2px}
.past-roles li::before{content:"";position:absolute;left:0;top:7px;width:5px;height:5px;border-radius:50%;background:var(--accent)}
.credentials{position:absolute;left:22px;top:767px;width:681px;display:grid;grid-template-columns:1fr 1fr;
  border:2px solid var(--accent)}
.credentials__col + .credentials__col{border-left:2px solid var(--accent)}
.credentials h3{background:var(--accent);color:#fff;font-family:"Montserrat",sans-serif;font-weight:600;
  font-size:15.5px;text-align:center;padding:7px 0 6px;letter-spacing:.4px}
.credentials ul{list-style:none;font-size:11px;line-height:13px}
.credentials li{display:flex;gap:8px;padding:5px 12px 4px;border-bottom:1px solid #bbb}
.credentials li:last-child{border-bottom:none}
.credentials svg{flex:none;width:10px;height:10px;margin-top:1px;stroke:var(--accent);fill:none;stroke-width:2}
</style>
</head>
<body>

<section class="page page--one">
  <header class="profile">
    <div class="profile__photo"><span role="img" aria-label="Portrait photo of Miriam Calder"></span></div>
    <h1 class="profile__name">MIRIAM CALDER</h1>
    <p class="profile__role">Senior Manager, Organisation Development Director.<br>Singapore, 538210</p>
    <ul class="profile__contact">
      <li><svg viewBox="0 0 24 24"><path d="M6.6 10.8a15.1 15.1 0 0 0 6.6 6.6l2.2-2.2c.3-.3.7-.4 1-.2 1.1.4 2.3.6 3.6.6.6 0 1 .4 1 1V20c0 .6-.4 1-1 1A17 17 0 0 1 3 4c0-.6.4-1 1-1h3.5c.6 0 1 .4 1 1 0 1.3.2 2.5.6 3.6.1.3 0 .7-.2 1z"/></svg>+ 65 9000 4812</li>
      <li><svg viewBox="0 0 24 24"><path d="M2 5h20v14H2z" style="fill:var(--accent)"/><path d="M2 6l10 7.5L22 6" stroke="#fff" stroke-width="1.6" fill="none"/></svg>miriamc@calderconsultingmail.com</li>
    </ul>
  </header>

  <div class="focus-band">HR STRATEGY | HR DAILY OPERATIONS | HR PROJECTS | TALENT MANAGEMENT | BUSINESS SOLUTIONS</div>

  <div class="summary">
    <p>My strength is in leadership and providing excellence in HR Operational Services, Recruiting, People Development and building high performing teams with energy and purpose.</p>
    <p>Masters in Strategic Organisational Development. As an authentic leader, I excel at navigating across the business to build a positive culture, consult with Senior Executives to understand their imperative business needs and recommend the best strategic solutions.</p>
    <p>Successfully worked on several projects with premium brands: Brisa Cola, TAURO, Crispy Barn and Dairyvale. The Brisa Cola project was a large scale project where we rolled our to 200 + new customer sites. Achieved all success factors including 20 + technical service agents, competency development, implementing an online digitalised application for customer reporting efficiency and achieved 100 % project completion.</p>
  </div>

  <h2 class="section-title skills-title">SKILLS</h2>
  <table class="skills">
    <tr><td>Human Resources Strategy</td><td>HR Policy and Process</td></tr>
    <tr><td>Human Resources Operations</td><td>Consulting, Stakeholder Management</td></tr>
    <tr><td>Recruitment Process, Talent Acquisition</td><td>Talent Management, &nbsp;Performance Management, &nbsp;Competency Development.</td></tr>
    <tr><td>Singapore, Employment Legislation &amp; Industrial Relations.</td><td>Australia, Fair Work, National Standards and Awards.</td></tr>
    <tr><td>HR Business Partner</td><td>HR Project Management</td></tr>
  </table>

  <footer class="page__footer">www.miriamcalder-profile.com/hr-leader</footer>
</section>

<section class="page page--two">
  <div class="page__strip"></div>
  <div class="education">
    <h2 class="section-title">EDUCATION</h2>
    <ul class="entry-list">
      <li><strong>Masters in Strategic Organisational Development</strong><br>Northfield University, Australia<br>December 2011 to December 2017</li>
      <li><strong>Management in Human Resources Certificate – Graduated with Distinction</strong><br>Pacific Coast University Extension Program, USA<br>June 2003 – November 2006</li>
      <li><strong>Bachelor of Business in Tourism Management</strong><br>Eastshore University, Australia<br>January 1992 to December 1996</li>
    </ul>
  </div>
  <div class="experience">
    <h2 class="section-title">WORK EXPERIENCE</h2>
    <p class="role-head">Senior Manager | Organisation Development Director, FMCG Industry<br>Calder Business Consulting | Singapore August 2015 to Present</p>
    <ul class="duties">
      <li>Delivered HR Strategy and Daily HR Operations, HR Policy, &nbsp;Recruitment, Performance Management and Communications.</li>
      <li>Leadership, Team Management to 20 + Technical Field Service Agents, FMCG/ F &amp; B Retail Project.</li>
      <li>Recruitment Process for MNCs – Brisa Cola, Crispy Barn and Tauro for large scale projects.</li>
      <li>HR Advisor to business leaders to achieve business strategic objectives.</li>
      <li>Worked with Senior Leaders in manpower planning, skill development and tracking.</li>
      <li>Developed action plans and strategies to support business needs, talent management,performance management check ins.</li>
      <li>HRBP, Stakeholder Management, Workforce Planning for NOVA Project Roll Out.<br>Project P + L Financial Management to &nbsp;SG $ 1.2 Million</li>
      <li>Digitalised online business solution by implementing FieldTrack System to value add, increase efficiency and reporting transparency to customers.</li>
      <li>Provide tools required for Team Members and training on new Service App system.</li>
      <li>Manage Performance Management Process check ins, which resulted in greater levels of engagement</li>
      <li>Oversee weekly payroll and summary report. Sign off on PAYG Tax and GST Report</li>
      <li>Educated new hires on expected job tasks, compensation and benefits to set clear expectations.</li>
      <li>Coaching on expected behaviours through consultations, job spec and code of business reference.</li>
      <li>Project Management - Managed multiple large scale projects across resourcing and daily operations requirements for Brisa Cola, TAURO, Crispy Barn, and Dairyvale. Delivered premium technical field services to 200 + equipment asset per month i.e 400 services/per month.</li>
      <li>Customer Service Survey Data Results = Highly Satisfied and Customer Net Promoter Score 100 %</li>
    </ul>
  </div>
  <footer class="page__footer">www.miriamcalder-profile.com/hr-leader</footer>
</section>

<section class="page page--three">
  <div class="page__strip"></div>
  <div class="continued">
    <p class="role-head">Clearway Pty. Ltd, Organisation Development Director, Client Relations, Clearway<br>Australia, June 2008 to August 2015</p>
    <ul class="duties">
      <li>Established Business Strategy in consultation with management.</li>
      <li>Delivered HR Strategy and daily hands on Human Resources Operations:</li>
      <li>Recruitment,Performance Management and Training and Development.</li>
      <li>Leadership to Team of 20 + resources, created a high performing service focused team.</li>
      <li>Client relations, effective communications and stakeholder management.</li>
      <li>Managed recruitment process for Equipment Field Services Team for MNCs Client Projects; Brisa Cola, Crispy Barn and Dairyvale</li>
      <li>Recruit new Service Provider contracts with Brisa Cola, Crispy Barn, &nbsp;and Dairyvale</li>
      <li>Project P + L Financial Management to &nbsp;SG $ 1.2 million.</li>
      <li>Workforce Planning on Technical Field Projects for Brisa Cola and Crispy Barn for resources across</li>
      <li>Managed multiple projects spanning across Australia, NSW, QLD, VIC and SA. Delivering technical field service to &gt;200 equipment assets i.e 400 + operational services performed each month.</li>
      <li>Focused on quality service results, delivering a positive customer service experience.</li>
    </ul>
    <p class="role-head">Director Career Services, Westmark College<br>USA, October 2003 to December 2007</p>
    <ul class="duties duties--spaced">
      <li>Brand expansion, Business Development, Marketing of Westmark College into San Francisco,Sacramento, Fremont, Santa Clara and the Bay Area.</li>
      <li>Built out the department from scratch, developed strategies, process and service standards.</li>
      <li>HR Strategy and Human Resource Operations: Recruitment, Job Placement, Performance</li>
      <li>Management, HR Policy, Training and Development.</li>
      <li>Graduate Program Placement for 700 + Medical graduates, MA, LVN and RN Program.</li>
      <li>Acquired new accounts from multiple hospitals and medical centres across the San Francisco Bay Area.</li>
      <li>Project Management with Senior Leadership Team for Board of Private Education Accreditation. Business Goal, engagement and contracts for preceptorships sites to facilitate L &amp; D.</li>
      <li>Awarded 2005 - Employee of the Year</li>
      <li>Account Management: Valley Health Group, Oakridge Medical Centre, Mission Park Medical Centre and Regional Veterans Health Office.</li>
    </ul>
    <ul class="past-roles">
      <li>Recruitment Consultant, Harbor Staffing, HealthCare and IT Industry<br>Australia, July 2002 to May 2003</li>
      <li>Recruitment Consultant, Netwise, IT Industry<br>Australia, July 2001 to May 2002</li>
      <li>Sales and IT Sourcer, Corelink Systems, IT Industry<br>Australia, April 2000 to April 2001</li>
    </ul>
  </div>

  <div class="credentials">
    <div class="credentials__col">
      <h3>PROFESSIONAL MEMBERSHIPS</h3>
      <ul>
        <li><svg viewBox="0 0 10 10"><path d="M1 5.5l2.5 2.5L9 2"/></svg>Member of Singapore People Practice Institute,<br>204 5817 2020</li>
        <li><svg viewBox="0 0 10 10"><path d="M1 5.5l2.5 2.5L9 2"/></svg>Member of Australian People Professionals Institute,<br>581263.</li>
      </ul>
    </div>
    <div class="credentials__col">
      <h3>CURRENT COURSES COMPLETED, 2020</h3>
      <ul>
        <li><svg viewBox="0 0 10 10"><path d="M1 5.5l2.5 2.5L9 2"/></svg>Singapore Employment Legislation and Industrial<br>Relations, SPPI, 2020.</li>
        <li><svg viewBox="0 0 10 10"><path d="M1 5.5l2.5 2.5L9 2"/></svg>Human Resource Analytics and Insights, SPPI, 2020.</li>
      </ul>
    </div>
  </div>

  <footer class="page__footer">www.miriamcalder-profile.com/hr-leader</footer>
</section>

</body>
</html>
```